Postcard Design Project

Company Name - Velmora Office Goods LLC We service and Repair printers, Fax and Copiers and sells all Business Technology supplies including supplies for Printers and Copiers to all NYC Metropolitan area.

Target Market(s)

NYC Small to Medium size business

Industry/Entity Type

Business

Font styles to use
Sans Serif

Colors

Designer to choose colors to be used in the design.

Requirements
Must have
• Printer Repairs and Toners Sales

```html
<!DOCTYPE html>
<html lang="en">
<head>
<meta charset="utf-8">
<title>Velmora Office Goods – Postcard</title>
<link rel="stylesheet" href="https://fonts.googleapis.com/css2?family=Exo+2:ital,wght@1,800;1,900&family=Lato:wght@400;700;900&display=swap">
<style>
  :root {
    --brand-blue: #2f5d9e;
    --brand-blue-dark: #244a80;
    --ink-gray: #4a4a4a;
    --band-gray: #6d6e71;
    --ring-gray: #6a6a6a;
    --paper: #ffffff;
    --backdrop: #a9a9a9;
    --accent-yellow: #f2c12e;
    --photo-steel: #8a8f96;
    --photo-light: #c9ccd1;
  }
  * { margin: 0; padding: 0; box-sizing: border-box; }
  html, body { width: 1200px; height: 950px; overflow: hidden; }
  body {
    background: var(--backdrop);
    font-family: "Lato", sans-serif;
    display: flex;
    align-items: center;
    justify-content: center;
    gap: 20px;
  }
  .postcard {
    position: relative;
    width: 570px;
    height: 380px;
    background: var(--paper);
    overflow: hidden;
  }
  .postcard__shapes { position: absolute; inset: 0; }

  /* Front */
  .front__headline {
    position: absolute; left: 40px; top: 28px;
    font-weight: 900; font-size: 60px; line-height: 0.95;
    color: var(--brand-blue); letter-spacing: -1px;
  }
  .front__offer {
    position: absolute; left: 30px; top: 156px;
    color: var(--paper); font-weight: 700; font-size: 15px; line-height: 1.3;
    white-space: nowrap;
  }
  .front__call-label {
    position: absolute; left: 30px; top: 224px;
    color: var(--ink-gray); font-weight: 700; font-size: 15px;
  }
  .front__phone {
    position: absolute; left: 28px; top: 242px;
    color: var(--ink-gray); font-weight: 700; font-size: 30px; letter-spacing: 0;
    white-space: nowrap;
  }
  .front__web-label {
    position: absolute; left: 26px; top: 302px;
    color: var(--paper); font-size: 15px;
  }
  .front__web {
    position: absolute; left: 24px; top: 324px;
    color: var(--paper); font-weight: 700; font-size: 20px;
    white-space: nowrap;
  }
  .badge {
    position: absolute; left: 240px; top: 151px; width: 164px; height: 164px;
    border-radius: 50%; border: 6px solid var(--ring-gray);
    background: var(--paper); overflow: hidden;
  }
  .badge__brand {
    position: absolute; top: 26px; left: 0; right: 0;
    display: flex; align-items: center; justify-content: center; gap: 5px;
    font-weight: 900; font-size: 13px; color: var(--brand-blue-dark); line-height: 1.05;
  }
  .brand-square { width: 16px; height: 16px; background: var(--brand-blue); flex: none; }
  .badge__cta {
    position: absolute; left: 0; right: 0; bottom: 0; height: 86px;
    background: var(--brand-blue); color: var(--paper);
    font-weight: 900; font-size: 14px; line-height: 1.15; text-align: center;
    padding-top: 12px;
  }

  /* Back */
  .back__offer {
    position: absolute; left: 18px; top: 138px; width: 270px;
    font-family: "Exo 2", sans-serif; font-style: italic; font-weight: 900;
    font-size: 15px; line-height: 1.05; color: var(--brand-blue); text-transform: uppercase;
  }
  .back__call-label {
    position: absolute; left: 18px; top: 210px;
    font-family: "Exo 2", sans-serif; font-style: italic; font-weight: 800;
    font-size: 12px; color: var(--paper);
  }
  .back__phone {
    position: absolute; left: 16px; top: 224px;
    font-family: "Exo 2", sans-serif; font-style: italic; font-weight: 900;
    font-size: 34px; color: var(--paper);
  }
  .back__web {
    position: absolute; left: 18px; top: 340px;
    font-family: "Exo 2", sans-serif; font-style: italic; font-weight: 900;
    font-size: 17px; color: var(--paper); letter-spacing: 1px;
  }
  .back__brand {
    position: absolute; left: 350px; top: 172px;
    display: flex; align-items: center; gap: 6px;
    font-weight: 900; font-size: 15px; color: var(--brand-blue-dark);
  }
</style>
</head>
<body>

  <section class="postcard postcard--front" aria-label="Postcard front">
    <svg class="postcard__shapes" width="570" height="380" viewBox="0 0 570 380">
      <polygon points="412,0 570,0 570,150 348,150" fill="var(--photo-steel)" role="img" aria-label="Photo of a gloved hand servicing printer internals"/>
      <polygon points="404,0 412,0 348,150 340,150" fill="var(--brand-blue)"/>
      <rect x="340" y="150" width="230" height="8" fill="var(--brand-blue)"/>
      <polygon points="340,158 570,158 570,380 250,380" fill="var(--photo-light)" role="img" aria-label="Photo of hands replacing a toner cartridge in an open printer"/>
      <polygon points="334,158 340,158 250,380 240,380" fill="var(--brand-blue)"/>
      <polygon points="14,148 348,148 320,212 14,212" fill="var(--brand-blue)"/>
      <polygon points="0,292 280,292 245,380 0,380" fill="var(--band-gray)"/>
    </svg>

    <h1 class="front__headline">GOT DIRTY<br>PRINTER?</h1>
    <p class="front__offer">Also check out our unbeatable<br>Ink and Toner online prices</p>
    <p class="front__call-label">CALL TODAY:</p>
    <p class="front__phone">718-555-0142</p>
    <p class="front__web-label">Visit us. Online</p>
    <p class="front__web">www.velmoragoods.com</p>

    <div class="badge">
      <div class="badge__brand"><span class="brand-square"></span><span>Velmora Office<br>Goods</span></div>
      <p class="badge__cta">GET A TECHNICIAN<br>IN YOUR OFFICE<br>TODAY</p>
    </div>
  </section>

  <section class="postcard postcard--back" aria-label="Postcard back">
    <svg class="postcard__shapes" width="570" height="380" viewBox="0 0 570 380">
      <rect x="0" y="0" width="285" height="128" fill="var(--photo-light)" role="img" aria-label="Photo of hands replacing toner cartridges in a printer"/>
      <rect x="0" y="128" width="285" height="66" fill="var(--accent-yellow)"/>
      <rect x="0" y="194" width="285" height="124" fill="var(--brand-blue)"/>
      <rect x="0" y="318" width="570" height="4" fill="var(--accent-yellow)"/>
      <rect x="0" y="322" width="570" height="58" fill="var(--brand-blue)"/>
      <rect x="285" y="0" width="10" height="318" fill="var(--photo-light)"/>
      <rect x="478" y="28" width="56" height="42" fill="#333333"/>
      <g stroke="#555555" stroke-width="1">
        <line x1="340" y1="232" x2="540" y2="232"/>
        <line x1="330" y1="260" x2="540" y2="260"/>
        <line x1="320" y1="288" x2="540" y2="288"/>
      </g>
    </svg>

    <p class="back__offer">Also check out our unbeatable ink and toner online prices</p>
    <p class="back__call-label">CALL TODAY:</p>
    <p class="back__phone">718-555-0142</p>
    <p class="back__web">VISIT US. ONLINE : WWW.VELMORAGOODS.COM</p>
    <div class="back__brand"><span class="brand-square"></span><span>Velmora Office Goods</span></div>
  </section>

</body>
</html>
```